Recycling and Rubbish services for Residential and Commercial customers

We are after a complete redesign or freshening up of our current website.
www.tidlowe.co.nz
On this site the general public can rent or buy rollaTUBs or skips for rubbish and recycling collection around the Nelson and Tasman area of New Zealand.

Target Market(s)

18 to 100 year old males and females in Nelson and Tasman area of New Zealand

Industry/Entity Type

Waste Management

Contact Information for Business Card

logo name title email phone web site address all the normal stuff

Number of Pages Required

5+ page

Colors

Designer to choose colors to be used in the design.

Requirements
Must have
• Has to be very fast and easy for the customer to rent bin, skip, tags, liner etc..
• see web site www.tidlowe.co.nz
• An address finder so we can show two rates for urban and rural streets
Nice to have
• "We’re trying to get back to a more human face. Our customers appreciate that we are locals too. We are proud to be able to support our local community through sponsorship and donations."

```html
<!DOCTYPE html>
<html lang="en">
<head>
<meta charset="utf-8">
<title>Tid Lowe – Putting Waste in its Place</title>
<link rel="stylesheet" href="https://fonts.googleapis.com/css2?family=Open+Sans:ital,wght@0,300;0,400;0,600;0,700;0,800;1,700&display=swap">
<style>
:root{
  --green:#0d6b34;
  --green-band:#1f7a43;
  --red:#e8384f;
  --ink:#333;
  --muted:#666;
  --panel:#ececec;
  --line:#dcdcdc;
  --footer:#111;
  --footer-bottom:#0a0a0a;
  --white:#fff;
}
*{box-sizing:border-box;margin:0;padding:0}
html,body{width:1200px;height:2667px;overflow:hidden}
body{font-family:"Open Sans",Arial,sans-serif;color:var(--ink);background:var(--white);position:relative}
.wrap{width:880px;margin:0 auto;position:relative}

/* top bar */
.topbar{height:32px;background:var(--green);color:var(--white);font-size:11px}
.topbar .wrap{display:flex;align-items:center;height:32px}
.topbar .contact{display:flex;align-items:center;gap:8px;padding:0 12px;height:32px;border-left:1px solid rgba(255,255,255,.25)}
.topbar .contact:last-of-type{border-right:1px solid rgba(255,255,255,.25)}
.topbar .contact .ico{width:16px;height:16px;border:1px solid var(--white);display:flex;align-items:center;justify-content:center}
.social{margin-left:auto;display:flex;gap:4px}
.social span{width:16px;height:16px;border:1px solid currentColor;display:block}

/* header */
.header{height:92px;border-bottom:1px solid #eee}
.header .wrap{display:flex;align-items:center;height:92px}
.brand{display:flex;align-items:center;gap:8px;font-weight:800;font-size:22px;color:var(--green);letter-spacing:.5px}
.brand .mark{width:22px;height:22px;background:var(--green)}
.nav{margin-left:auto;display:flex;gap:6px;font-size:11px;text-transform:uppercase}
.nav a{color:#555;text-decoration:none;padding:6px 12px}
.nav a.active{background:var(--red);color:var(--white)}

/* hero */
.hero{position:relative;height:564px;background:linear-gradient(180deg,#e9e9e9 0%,#dcdcdc 60%,#a9a9a9 100%);text-align:center}
.hero-photo{position:absolute;inset:0}
.hero h1{position:relative;padding-top:66px;font-size:44px;font-weight:800;letter-spacing:5px;color:var(--green)}
.hero p{position:relative;width:460px;margin:8px auto 0;font-size:14px;letter-spacing:1.2px;line-height:20px;color:#222}
.hero .arrow{position:absolute;top:246px;width:62px;height:62px;background:var(--green);display:flex;align-items:center;justify-content:center}
.hero .arrow.left{left:0}.hero .arrow.right{right:0}

/* location band */
.location{height:73px;background:var(--red);color:var(--white)}
.location .wrap{display:flex;align-items:center;justify-content:center;height:73px;gap:14px;font-size:15px}
.location .btn{margin-left:28px;border:1px solid var(--white);padding:7px 14px;font-size:12px;letter-spacing:1px}

/* services */
.services{padding-top:43px}
.services .grid{display:grid;grid-template-columns:repeat(3,277px);gap:25px 24px}
.service{background:var(--panel);height:165px;padding:16px 14px 0}
.service.featured{background:var(--white);box-shadow:0 2px 12px rgba(0,0,0,.2)}
.service h3{text-align:center;font-size:13px;font-weight:600;letter-spacing:2px;text-transform:uppercase}
.service .rule{width:7px;height:7px;background:var(--green);margin:12px auto 0}
.service .hr{border-top:1px solid var(--line);margin-top:-4px}
.service .body{display:flex;gap:14px;margin-top:16px;align-items:flex-start}
.service .icon{flex:0 0 54px;height:62px;display:flex;align-items:center;justify-content:center}
.service p{font-size:10.5px;line-height:18px;color:#444}

/* product sections */
.section-title{text-align:center;font-size:21px;font-weight:400;letter-spacing:2.5px;color:#666;text-transform:uppercase}
.section-title:after{content:"";display:block;width:40px;height:3px;background:var(--green);margin:8px auto 0}
.products{padding-top:50px}
.quick{padding-top:38px}
.cards{display:grid;grid-template-columns:repeat(4,203px);gap:23px;margin-top:28px}
.card{height:262px;border:1px solid #e2e2e2;display:flex;flex-direction:column}
.card .thumb{flex:1;margin:22px 24px}
.card .btn{height:45px;background:var(--red);color:var(--white);font-size:9.5px;font-weight:700;text-transform:uppercase;display:flex;align-items:center;justify-content:center;gap:8px}
.card .btn .dot{width:10px;height:10px;border-radius:50%;background:var(--white);position:relative}
.card .btn .dot:after{content:"";position:absolute;left:3px;top:3px;border-left:4px solid var(--red);border-top:2px solid transparent;border-bottom:2px solid transparent}
.thumb.bin{background:linear-gradient(180deg,#3d7a4a,#23502f)}
.thumb.skip{background:linear-gradient(180deg,#3f8a52,#255d34)}
.thumb.supplies{background:linear-gradient(135deg,#d8e06a,#3d6fb0 60%,#e8e8e8)}
.thumb.bag{background:linear-gradient(180deg,#f2f2f2,#cfcfcf)}
.thumb.tag{background:linear-gradient(180deg,#4aa3df,#2d7fbf)}

/* testimonial */
.testimonial{position:absolute;top:1947px;left:0;width:1200px;height:373px;background:var(--green-band);color:var(--white);text-align:center}
.testimonial h2{padding-top:42px;font-size:19px;font-weight:400;letter-spacing:2.5px}
.testimonial h2:after{content:"";display:block;width:34px;height:2px;background:var(--white);margin:6px auto 0}
.avatar{width:92px;height:92px;border-radius:50%;background:linear-gradient(180deg,#d9b9a3,#7b5a4a);border:3px solid var(--white);margin:25px auto 0}
.testimonial blockquote{width:690px;margin:20px auto 0;font-size:11.5px;line-height:19px}
.testimonial cite{display:block;margin-top:12px;font-size:11.5px;font-weight:700;font-style:italic}
.dots{display:flex;justify-content:center;gap:6px;margin-top:26px}
.dots span{width:14px;height:3px;background:rgba(255,255,255,.5)}
.dots span.on{background:var(--red)}

/* footer */
.footer{position:absolute;top:2320px;left:0;width:1200px;height:272px;background:var(--footer);color:#ccc;font-size:10.5px}
.footer .cols{display:grid;grid-template-columns:226px 226px 224px 204px;padding-top:38px}
.footer h4{color:var(--white);font-size:12px;font-weight:600;text-transform:uppercase;padding-bottom:6px;display:inline-block;border-bottom:2px solid var(--green)}
.footer .brand{color:var(--white)}
.footer .about p{margin-top:30px;width:200px;line-height:16px}
.footer ul{list-style:none;margin-top:16px}
.footer li{line-height:24px}
.footer li:before{content:"›";margin-right:12px}
.footer .touch .row{display:flex;gap:18px;margin-top:18px;line-height:15px;width:200px}
.footer .touch .row:first-of-type{margin-top:22px}
.footer .news p{margin-top:16px;line-height:16px}
.footer .subscribe{margin-top:12px;display:flex;border:1px solid #555;height:34px;width:200px}
.footer .subscribe span{flex:1;padding:9px 8px;font-size:10px;color:#bbb}
.footer .subscribe i{width:32px;border-left:1px solid #555;display:flex;align-items:center;justify-content:center;font-style:normal;color:var(--white)}
.footer .follow{margin-top:14px}
.footer .social{margin:12px 0 0;justify-content:flex-start}
.footer .social span{width:22px;height:22px;border-color:#777}
.bottombar{position:absolute;top:2592px;left:0;width:1200px;height:75px;background:var(--footer-bottom);color:#aaa;font-size:10.5px}
.bottombar .wrap{display:flex;align-items:center;height:75px}
.bottombar .legal{margin-left:auto}
</style>
</head>
<body>

<div class="topbar">
  <div class="wrap">
    <div class="contact"><span class="ico"><svg width="9" height="9" viewBox="0 0 10 10"><path d="M2 1l2 2-1 1.5c.8 1.4 1.6 2.2 3 3L7.5 6l2 2-1.5 1.5C4.5 9 1 5.5.5 2.5z" fill="#fff"/></svg></span>(03) 555 0148</div>
    <div class="contact"><span class="ico"><svg width="10" height="8" viewBox="0 0 10 8"><rect x=".5" y=".5" width="9" height="7" fill="none" stroke="#fff"/><path d="M.5.5l4.5 4 4.5-4" fill="none" stroke="#fff"/></svg></span>info@tidlowe.co.nz</div>
    <div class="social"><span></span><span></span><span></span></div>
  </div>
</div>

<header class="header">
  <div class="wrap">
    <div class="brand"><span class="mark"></span>TID LOWE</div>
    <nav class="nav">
      <a class="active" href="#">Home</a><a href="#">About</a><a href="#">Services</a><a href="#">Media</a><a href="#">FAQ</a><a href="#">Contact</a>
    </nav>
  </div>
</header>

<section class="hero">
  <div class="hero-photo" role="img" aria-label="Green, black and blue rollaTUBs standing in front of a white brick wall"></div>
  <h1>PUTTING WASTE IN ITS PLACE</h1>
  <p>TID LOWE is the only locally owned and operated waste collection service in Nelson and being the largest rollaTUB operator in the Nelson Tasman District</p>
  <div class="arrow left"><svg width="12" height="14" viewBox="0 0 12 14"><path d="M9 1L3 7l6 6" fill="none" stroke="#fff" stroke-width="2.5"/></svg></div>
  <div class="arrow right"><svg width="12" height="14" viewBox="0 0 12 14"><path d="M3 1l6 6-6 6" fill="none" stroke="#fff" stroke-width="2.5"/></svg></div>
</section>

<section class="location">
  <div class="wrap">
    <svg width="18" height="24" viewBox="0 0 18 24"><path d="M9 0a9 9 0 0 0-9 9c0 6.5 9 15 9 15s9-8.5 9-15a9 9 0 0 0-9-9zm0 12.5A3.5 3.5 0 1 1 9 5.5a3.5 3.5 0 0 1 0 7z" fill="#fff"/></svg>
    <span>Tid Lowe - 41 Harbour Lane, New Zealand</span>
    <span class="btn">CHANGE LOCATION</span>
  </div>
</section>

<section class="services">
  <div class="wrap grid">
    <div class="service"><h3>Product Range</h3><div class="rule"></div><div class="hr"></div>
      <div class="body"><div class="icon"><svg width="40" height="52" viewBox="0 0 40 52" fill="none" stroke="#444" stroke-width="2"><path d="M6 18h26l-3 28H9z"/><path d="M4 18h30"/><circle cx="10" cy="47" r="3"/><circle cx="28" cy="8" r="3"/><circle cx="20" cy="5" r="2"/></svg></div>
      <p>Lorem ipsum dolor sit amet, consectetur adipiscing elit, sed do eiusmod tempor incididunt ut labore et dolore.</p></div></div>
    <div class="service featured"><h3>Collection Area/ Days</h3><div class="rule"></div><div class="hr"></div>
      <div class="body"><div class="icon"><svg width="40" height="50" viewBox="0 0 40 50"><path d="M20 2a13 13 0 0 0-13 13c0 10 13 22 13 22s13-12 13-22A13 13 0 0 0 20 2zm0 18a5 5 0 1 1 0-10 5 5 0 0 1 0 10z" fill="#444"/><ellipse cx="20" cy="44" rx="18" ry="4" fill="none" stroke="#444" stroke-width="2"/></svg></div>
      <p>Lorem ipsum dolor sit amet, consectetur adipiscing elit, sed do eiusmod tempor incididunt ut labore et dolore.</p></div></div>
    <div class="service"><h3>Pay My Account</h3><div class="rule"></div><div class="hr"></div>
      <div class="body"><div class="icon"><svg width="40" height="44" viewBox="0 0 40 44"><circle cx="16" cy="11" r="9" fill="#444"/><path d="M0 40c0-12 7-18 16-18s16 6 16 18z" fill="#444"/><circle cx="30" cy="34" r="9" fill="#444" stroke="#ececec" stroke-width="2"/><text x="30" y="38" font-size="12" text-anchor="middle" fill="#fff" font-family="Open Sans, sans-serif">$</text></svg></div>
      <p>Lorem ipsum dolor sit amet, consectetur adipiscing elit, sed do eiusmod tempor incididunt ut labore et dolore.</p></div></div>

    <div class="service"><h3>Change My Bin Size</h3><div class="rule"></div><div class="hr"></div>
      <div class="body"><div class="icon"><svg width="40" height="52" viewBox="0 0 40 52" fill="none" stroke="#444" stroke-width="2"><path d="M6 18h26l-3 28H9z"/><path d="M4 18h30"/><circle cx="10" cy="47" r="3"/><path d="M14 38l10-10M20 28h4v4"/><circle cx="28" cy="8" r="3"/></svg></div>
      <p>Lorem ipsum dolor sit amet, consectetur adipiscing elit, sed do eiusmod tempor incididunt ut labore et dolore.</p></div></div>
    <div class="service"><h3>Change My Address</h3><div class="rule"></div><div class="hr"></div>
      <div class="body"><div class="icon"><svg width="44" height="40" viewBox="0 0 44 40" fill="none" stroke="#444" stroke-width="2"><path d="M2 20L22 2l20 18"/><path d="M7 16v22h30V16"/><path d="M18 38V26h8v12"/></svg></div>
      <p>Lorem ipsum dolor sit amet, consectetur adipiscing elit, sed do eiusmod tempor incididunt ut labore et dolore.</p></div></div>
    <div class="service"><h3>Public Holiday Collection</h3><div class="rule"></div><div class="hr"></div>
      <div class="body"><div class="icon"><svg width="46" height="44" viewBox="0 0 46 44"><rect x="10" y="6" width="34" height="32" fill="none" stroke="#444" stroke-width="2"/><rect x="10" y="6" width="34" height="7" fill="#444"/><g fill="#444"><rect x="15" y="17" width="5" height="4"/><rect x="24" y="17" width="5" height="4"/><rect x="33" y="17" width="5" height="4"/><rect x="15" y="25" width="5" height="4"/><rect x="24" y="25" width="5" height="4"/><rect x="33" y="25" width="5" height="4"/></g><path d="M2 30l10-5v16L2 36z" fill="#444"/></svg></div>
      <p>Lorem ipsum dolor sit amet, consectetur adipiscing elit, sed do eiusmod tempor incididunt ut labore et dolore.</p></div></div>
  </div>
</section>

<section class="products">
  <div class="wrap">
    <h2 class="section-title">Our Products</h2>
    <div class="cards">
      <div class="card"><div class="thumb bin" role="img" aria-label="Dark green rollaTUB"></div><div class="btn">Get your bin here <span class="dot"></span></div></div>
      <div class="card"><div class="thumb skip" role="img" aria-label="Green skip bin"></div><div class="btn">Get your skip here <span class="dot"></span></div></div>
      <div class="card"><div class="thumb bin" role="img" aria-label="Large green commercial bin on wheels"></div><div class="btn">Get comercial bin <span class="dot"></span></div></div>
      <div class="card"><div class="thumb supplies" role="img" aria-label="Bin supplies: liners, tags and stickers"></div><div class="btn">Get bin supplies <span class="dot"></span></div></div>
    </div>
  </div>
</section>

<section class="quick">
  <div class="wrap">
    <h2 class="section-title">Quick Buy</h2>
    <div class="cards">
      <div class="card"><div class="thumb bag" role="img" aria-label="Clear rubbish bag"></div><div class="btn">Quick buy <span class="dot"></span></div></div>
      <div class="card"><div class="thumb bin" role="img" aria-label="Green 120 litre rollaTUB"></div><div class="btn">Quick buy <span class="dot"></span></div></div>
      <div class="card"><div class="thumb bin" role="img" aria-label="Green 240 litre rollaTUB"></div><div class="btn">Quick buy <span class="dot"></span></div></div>
      <div class="card"><div class="thumb tag" role="img" aria-label="Blue 120 litre collection tag"></div><div class="btn">Quick buy <span class="dot"></span></div></div>
    </div>
  </div>
</section>

<section class="testimonial">
  <h2>CLIENT SPEAK</h2>
  <div class="avatar" role="img" aria-label="Portrait of the client"></div>
  <blockquote>Lorem ipsum dolor sit amet, consectetur adipiscing elit. Nullam pharetra sem at augue suscipit venenatis. Pellentesque mattis purus porttitor elit sagittis euismod. Vivamus ac ipsum vitae diam euismod consequat.
    <cite>- Maren Ellis</cite></blockquote>
  <div class="dots"><span></span><span class="on"></span><span></span></div>
</section>

<footer class="footer">
  <div class="wrap cols">
    <div class="about">
      <div class="brand"><span class="mark"></span>TID LOWE</div>
      <p>Lorem ipsum dolor sit amet, consectetur adipiscing elit. Nullam pharetra sem at augue suscipit venenatis. Pellentesque mattis purus porttitor elit sagittis euismod. Vivamus ac ipsum vitae diam euismod consequat.</p>
    </div>
    <div>
      <h4>Quick Links</h4>
      <ul><li>Home</li><li>About us</li><li>FAQ</li><li>Media</li><li>Links</li><li>Contact us</li></ul>
    </div>
    <div class="touch">
      <h4>Get in Touch</h4>
      <div class="row"><svg width="10" height="14" viewBox="0 0 18 24"><path d="M9 0a9 9 0 0 0-9 9c0 6.5 9 15 9 15s9-8.5 9-15a9 9 0 0 0-9-9zm0 12.5A3.5 3.5 0 1 1 9 5.5a3.5 3.5 0 0 1 0 7z" fill="#ccc"/></svg><span>Tid Lowe - 41 Harbour Lane - Nelson New Zealand</span></div>
      <div class="row" style="margin-top:28px"><svg width="11" height="11" viewBox="0 0 10 10"><path d="M2 1l2 2-1 1.5c.8 1.4 1.6 2.2 3 3L7.5 6l2 2-1.5 1.5C4.5 9 1 5.5.5 2.5z" fill="#ccc"/></svg><span>(03) 555 0148</span></div>
      <div class="row" style="margin-top:38px"><svg width="11" height="9" viewBox="0 0 10 8"><rect width="10" height="8" fill="#ccc"/><path d="M0 0l5 4 5-4" fill="none" stroke="#111"/></svg><span>info@tidlowe.co.nz</span></div>
    </div>
    <div class="news">
      <h4>Newsletter</h4>
      <p>Lorem ipsum dolor sit amet, consectetur adipiscing elit. Nullam pharetra sem at augue suscipit venenatis.</p>
      <div class="subscribe"><span>Enter your email address</span><i>›</i></div>
      <h4 class="follow">Follow us on</h4>
      <div class="social"><span></span><span></span><span></span></div>
    </div>
  </div>
</footer>

<div class="bottombar">
  <div class="wrap">
    <span>© 2017 Tidlowe. All right reserved</span>
    <span class="legal">Privacy Policy &nbsp; | &nbsp; Terms of Use</span>
  </div>
</div>

</body>
</html>
```